Redesign popular non profit computer donation and recycling website

We wish to make our website more high tech, more modern and feature all of our wonderful stories and offerings in easy to navigate location

Design will need to implement some dynamic variables, such as lists of charities, depot locations, and current content management system, folio grove pro

We wish to feature all of ojr media videos on the front page as well as the most recent donations

we wish to highlight our service offerings, hard drive shredding, volunteer to earn programs, computer store, etc

many of these great things are hard to find on the current layout

There is 2 designs that really catch our attention and we want to improve on both of those

Can we make the bottom blue?

How will the images that are in circles be rotated?

Can we make the latest donations section , 2/3 how it is of the page, and 1/3 make a section for Media, which will include all of our media highlights (vidlorn videos)

We really would like to feature our vidlorn videos on the front page

Can we add a live blurbix feed to the website.

Can we see how you will implement the depot locations inside of this design?
Can we see how you will implement the computer store with this design?
Currently located to www.umk.ca / login / wholesale / computer store shopping cart link

Can we see how you will change the contact us page
Can we see how you plan to display the list of waiting charities
Can we see how you plan to display all of our news feature articles 
Can we see how you plan to display our data destruction page

As we near the end of the contest I'd like to ask the designers the following;

The website must use h1,h2,h3,h4 in hierarchy only.. not starting with h6 or something random.. heading tags must only be used for actual headings.. html5 required, jquery installed and all elements of the design programmed in jquery only.. make sure lists are used in html whenever realistic.. no inline styles.... no classes added to paragraph, heading, or list elements allowed.

Target Market(s)

corporate donors
individuals
charities and non profits
low income people who wish to volunteer and earn a computer or laptop

Industry/Entity Type

Recycling

Requirements
Must have
• current umk logo
• high tech servers, laptops, velto switches, etc
• hard drive shredder in action
• all media stories and videos featured
• all latest donations scrolling
Nice to have
• corporate donors
• individuals
• charities and non profits
• low income people who wish to volunteer and earn a computer or laptop

```html
<!DOCTYPE html>
<html lang="en">
<head>
<meta charset="utf-8">
<title>umk – Home</title>
<link rel="stylesheet" href="https://fonts.googleapis.com/css2?family=Roboto:ital,wght@0,400;0,700;1,700&family=Oswald:wght@600&display=swap">
<style>
:root{
  --page-grey:#b7bdc1;
  --glow:#00e48c;
  --night:#030806;
  --bar:#050808;
  --panel:#4b4b4b;
  --strip:#a7a7a7;
  --white:#ffffff;
  --ink:#3a3a3a;
  --green:#0f9a6a;
  --title-green:#18b07a;
  --silver-top:#f2f2f2;
  --silver-bottom:#8f8f8f;
  --player:#3d3d3d;
}
*{margin:0;padding:0;box-sizing:border-box}
html,body{width:1200px;height:824px;overflow:hidden}
body{background:var(--page-grey);font-family:"Roboto",Arial,sans-serif;position:relative}
.hero-band{position:absolute;left:0;top:36px;width:1200px;height:538px;
  background:radial-gradient(ellipse 640px 420px at 600px 40px,var(--glow) 0%,#00a866 35%,#014528 65%,var(--night) 100%)}
.brand{position:absolute;left:500px;top:100px;width:200px;text-align:center;font-size:22px;font-weight:700;color:var(--white);letter-spacing:2px}
.top-nav{position:absolute;left:163px;top:179px;width:672px;height:34px;background:var(--bar)}
.top-nav ul{list-style:none}
.top-nav li{position:absolute;top:0;height:34px;line-height:30px;color:var(--white);font-size:15px;transform:translateX(-50%)}
.top-nav li:nth-child(1){left:133px}
.top-nav li:nth-child(2){left:244px}
.top-nav li:nth-child(3){left:361px}
.top-nav li:nth-child(4){left:478px}
.top-nav li:nth-child(5){left:607px}
.nav-rules{position:absolute;left:0;top:0}
.side-nav{position:absolute;left:835px;top:179px;width:192px}
.side-nav ul{list-style:none}
.side-nav li{height:37.5px;border:1px solid #555;background:linear-gradient(var(--silver-top),#cfcfcf 50%,var(--silver-bottom));
  font-size:17px;color:#1e1e1e;text-align:center;line-height:35px}
.side-extra{position:absolute;left:835px;top:552px;width:192px;height:272px;background:var(--night)}
.promo{position:absolute;left:20px;width:147px;border:3px solid var(--white)}
.promo-support{top:12px;height:106px;background:linear-gradient(135deg,#e8eef3,#b8c6d2)}
.promo-vote{top:133px;height:122px;background:var(--white);padding:10px 8px;color:#111}
.vote-title{font-family:"Roboto",sans-serif;font-weight:700;font-size:22px;line-height:22px}
.vote-title span{font-size:17px}
.vote-sub{font-size:8px;font-weight:700;margin-top:6px;line-height:10px}
.vote-site{font-size:8px;color:#7a2a8a;font-weight:700;line-height:10px}
.vote-foot{font-size:5px;margin-top:12px;padding-left:10px;color:#333}
.vote-tiles{position:absolute;right:0;top:0;width:52px;height:116px;background:linear-gradient(160deg,#6a3fa0,#2a7fd0 45%,#4cb85a)}
.row{position:absolute;left:163px;width:672px}
.aside-panel{position:absolute;left:0;top:0;width:196px;height:100%;background:var(--panel);color:var(--white);padding:0 10px}
.main-panel{position:absolute;left:196px;top:0;width:476px;height:100%;background:var(--white)}
.row-top{top:213px;height:220px}
.row-bottom{top:602px;height:222px}
.aside-panel h2{font-style:italic;font-weight:700;color:var(--title-green);font-size:21px;margin-top:8px;line-height:24px}
.aside-panel p{font-size:9.3px;line-height:9.5px;margin-top:4px;width:176px}
.aside-panel h3{font-size:12px;margin-top:10px;font-weight:700}
.fees{list-style:none;width:124px;margin-top:16px;font-size:9px;line-height:9.5px}
.fees li{display:flex;justify-content:space-between}
.row-bottom .aside-panel h2{font-style:normal;font-weight:400;color:var(--white);font-size:13px;margin-top:8px}
.perks{list-style:none;margin-top:14px;font-size:9px;line-height:9.3px;width:172px;letter-spacing:.2px}
.perks li{padding-left:6px;text-indent:-6px}
.perks li::before{content:"· "}
.story{position:absolute;left:16px;width:200px;color:var(--ink);font-size:8.6px;line-height:9.5px;letter-spacing:.35px}
.story h3{display:inline;font-size:12px;font-weight:400;letter-spacing:0}
.story-top{top:47px}
.story-bottom{top:18px}
.main-panel h2{position:absolute;left:16px;top:16px;color:var(--green);font-weight:400;font-size:18px}
.photo{position:absolute}
.photo-one{left:221px;top:28px;width:229px;height:167px;background:linear-gradient(135deg,#c9b59a,#8f8770 55%,#bda77c)}
.photo-two{left:222px;top:22px;width:229px;height:166px;background:linear-gradient(135deg,#4f6a52,#b9b7a5 50%,#2f2c2a)}
.video-strip{position:absolute;left:163px;top:433px;width:672px;height:169px;background:var(--strip)}
.video-strip h2{position:absolute;left:45px;top:2px;font-family:"Oswald",sans-serif;font-size:16px;color:#eeeeee;font-weight:600}
.arrow{position:absolute;top:66px}
.arrow-prev{left:7px}
.arrow-next{left:632px;top:64px}
.videos{list-style:none}
.video{position:absolute;top:27px;width:136px;height:114px;background:var(--player)}
.video:nth-child(1){left:46px}
.video:nth-child(2){left:197px}
.video:nth-child(3){left:347px}
.video:nth-child(4){left:496px}
.video-title{height:23px;background:#1b1b1b;color:var(--white);font-size:10px;line-height:23px;padding-left:9px;white-space:nowrap;overflow:hidden;width:108px}
.video-thumb{position:absolute;left:0;top:23px;width:136px;height:62px;background:linear-gradient(135deg,#7d8a90,#c9c6bd 55%,#55504a)}
.video svg{position:absolute;left:0;top:0}
</style>
</head>
<body>
<div class="hero-band"></div>
<header class="brand">umk</header>

<nav class="top-nav">
  <svg class="nav-rules" width="672" height="34"><g fill="#fff"><rect x="77" y="5" width="2" height="19"/><rect x="187" y="5" width="2" height="19"/><rect x="297" y="5" width="2" height="19"/><rect x="413" y="5" width="2" height="19"/><rect x="545" y="5" width="2" height="19"/></g></svg>
  <ul>
    <li>pickup</li>
    <li>donate</li>
    <li>recycle</li>
    <li>charities</li>
    <li>login</li>
  </ul>
</nav>

<nav class="side-nav">
  <ul>
    <li>About Us</li><li>Drop off items</li><li>Depots</li><li>Jobs</li><li>Volunteer</li>
    <li>Pictures and Videos</li><li>Links</li><li>Memberships</li><li>News</li><li>Contact us</li>
  </ul>
</nav>

<aside class="side-extra">
  <div class="promo promo-support" role="img" aria-label="Live support banner with a support agent wearing a headset"></div>
  <div class="promo promo-vote">
    <div class="vote-tiles" role="img" aria-label="Colourful geometric award pattern"></div>
    <div class="vote-title">VOTE<br><span>FOR US!</span></div>
    <div class="vote-sub">UNTIL NOV 30</div>
    <div class="vote-site">bizvoteawards.ca<br>#bizvoteawards</div>
    <div class="vote-foot">REGIONAL TRADE AWARDS</div>
  </div>
</aside>

<section class="row row-top">
  <div class="aside-panel">
    <h2>Donate</h2>
    <p>There are many reasons why an UMK annual membership will benefit your business. Please see below the three plans we offer to our clients.<br>Once your membership request is filled and processed, UMK will send you an honorary membership certificate to display in your office!<br>Please choose the type of membership you would like.</p>
    <h3>Regular:</h3>
    <ul class="fees">
      <li><span>Business</span><span>$100</span></li>
      <li><span>Schools, Hospitals</span><span>$75</span></li>
      <li><span>Government</span><span>$200</span></li>
      <li><span>Non profit</span><span>$75</span></li>
      <li><span>Personal</span><span>$50</span></li>
    </ul>
  </div>
  <div class="main-panel">
    <h2>our activity</h2>
    <div class="story story-top"><h3>December 2013</h3> - &nbsp;In Calgary, the UMK makes a donation of laptops and computers to Brightpath Special Needs Resource Centre. "These are a much needed upgrade from some of our current computers. Thank you so much UMK for this great donation! We really appreciate it - just look how excited Dana [Moore] is." Brightpath has been providing hope, guidance, and support to families who have children with special needs since 1985.</div>
    <div class="photo photo-one" role="img" aria-label="Charity staff member giving a thumbs up beside a donated box of computers"></div>
  </div>
</section>

<section class="video-strip">
  <h2>LATEST VIDEOS</h2>
  <svg class="arrow arrow-prev" width="34" height="34" viewBox="0 0 34 34"><circle cx="17" cy="17" r="16" fill="#e4efec" stroke="#6f8f86" stroke-width="1.5"/><path d="M21 9 L11 17 L21 25" fill="none" stroke="#445" stroke-width="4"/></svg>
  <svg class="arrow arrow-next" width="34" height="34" viewBox="0 0 34 34"><circle cx="17" cy="17" r="16" fill="#e4efec" stroke="#6f8f86" stroke-width="1.5"/><path d="M13 9 L23 17 L13 25" fill="none" stroke="#445" stroke-width="4"/></svg>
  <ul class="videos">
    <li class="video"><div class="video-title">Computer Donations</div><div class="video-thumb" role="img" aria-label="Video still of a technician in a computer workshop"></div>
      <svg width="136" height="114"><circle cx="128" cy="8" r="2" fill="#fff"/><circle cx="121" cy="12" r="2" fill="#fff"/><circle cx="128" cy="16" r="2" fill="#fff"/><path d="M128 8L121 12L128 16" stroke="#fff" fill="none"/><rect x="55" y="45" width="30" height="21" rx="4" fill="#1b1b1b"/><path d="M66 50l9 5.5-9 5.5z" fill="#fff"/><circle cx="7" cy="88" r="4" fill="#e3d5d5"/><path d="M18 97l9 6-9 6z" fill="#ccc"/><path d="M49 100h3l4-3v12l-4-3h-3z" fill="#ccc"/><text x="72" y="107" font-size="9" fill="#ddd">0:00 / 1:45</text><path d="M121 97h-3v3M127 97h3v3M121 109h-3v-3M127 109h3v-3" stroke="#ccc" fill="none"/></svg></li>
    <li class="video"><div class="video-title">www.umk.ca - reuse</div><div class="video-thumb" role="img" aria-label="Video still of volunteers working at computers"></div>
      <svg width="136" height="114"><circle cx="128" cy="8" r="2" fill="#fff"/><circle cx="121" cy="12" r="2" fill="#fff"/><circle cx="128" cy="16" r="2" fill="#fff"/><path d="M128 8L121 12L128 16" stroke="#fff" fill="none"/><rect x="55" y="45" width="30" height="21" rx="4" fill="#1b1b1b"/><path d="M66 50l9 5.5-9 5.5z" fill="#fff"/><circle cx="7" cy="88" r="4" fill="#e3d5d5"/><path d="M18 97l9 6-9 6z" fill="#ccc"/><path d="M49 100h3l4-3v12l-4-3h-3z" fill="#ccc"/><text x="72" y="107" font-size="9" fill="#ddd">0:00 / 1:32</text><path d="M121 97h-3v3M127 97h3v3M121 109h-3v-3M127 109h3v-3" stroke="#ccc" fill="none"/></svg></li>
    <li class="video"><div class="video-title">UMK Calgary Alberta</div><div class="video-thumb" role="img" aria-label="Video still of a television news interview"></div>
      <svg width="136" height="114"><circle cx="128" cy="8" r="2" fill="#fff"/><circle cx="121" cy="12" r="2" fill="#fff"/><circle cx="128" cy="16" r="2" fill="#fff"/><path d="M128 8L121 12L128 16" stroke="#fff" fill="none"/><rect x="55" y="45" width="30" height="21" rx="4" fill="#1b1b1b"/><path d="M66 50l9 5.5-9 5.5z" fill="#fff"/><circle cx="7" cy="88" r="4" fill="#e3d5d5"/><path d="M18 97l9 6-9 6z" fill="#ccc"/><path d="M49 100h3l4-3v12l-4-3h-3z" fill="#ccc"/><text x="72" y="107" font-size="9" fill="#ddd">0:00 / 2:12</text><path d="M121 97h-3v3M127 97h3v3M121 109h-3v-3M127 109h3v-3" stroke="#ccc" fill="none"/></svg></li>
    <li class="video"><div class="video-title">Computer Donations</div><div class="video-thumb" role="img" aria-label="Video still of a technician in a computer workshop"></div>
      <svg width="136" height="114"><circle cx="128" cy="8" r="2" fill="#fff"/><circle cx="121" cy="12" r="2" fill="#fff"/><circle cx="128" cy="16" r="2" fill="#fff"/><path d="M128 8L121 12L128 16" stroke="#fff" fill="none"/><rect x="55" y="45" width="30" height="21" rx="4" fill="#1b1b1b"/><path d="M66 50l9 5.5-9 5.5z" fill="#fff"/><circle cx="7" cy="88" r="4" fill="#e3d5d5"/><path d="M18 97l9 6-9 6z" fill="#ccc"/><path d="M49 100h3l4-3v12l-4-3h-3z" fill="#ccc"/><text x="72" y="107" font-size="9" fill="#ddd">0:00 / 1:45</text><path d="M121 97h-3v3M127 97h3v3M121 109h-3v-3M127 109h3v-3" stroke="#ccc" fill="none"/></svg></li>
  </ul>
</section>

<section class="row row-bottom">
  <div class="aside-panel">
    <h2>Benefits:</h2>
    <ul class="perks">
      <li>Priority pick-up dates</li>
      <li>Guaranteed pick-up on scheduled dates, priority over non-members</li>
      <li>Certification of collected equipment &amp; Data wipe certification</li>
      <li>Full consulting services</li>
      <li>35% discount on pick-up fees on low value donations</li>
      <li>Complimentary pick up services for high value donations</li>
      <li>Reduced rate (~$25) for floor model units (Photocopiers etc) Regular !</li>
    </ul>
  </div>
  <div class="main-panel">
    <div class="story story-bottom"><h3>November 2013</h3> – UMK grants the wish of a client of Camp Alder in BC. Mirela and her adorable five-year-son Tobias are coping with the loss of a loving husband and father, and were in need of a laptop for home use. Camp Alder offers bereavement care through counseling, support groups, camps and retreats to individuals and families dealing with loss of loved ones. The organization also holds Grief and Loss Workshops for health care professionals, teachers, and community groups.</div>
    <div class="photo photo-two" role="img" aria-label="Two women holding donated laptops beside a holiday tree"></div>
  </div>
</section>
</body>
</html>
```